Modernise Business Card

Our company has been operating for 10 years. With the start of the new decade we are looking to refresh our business card design. We manufacture a range of industrial product shipping to customers internationally. A copy of our current card, both sides, is attached. We are looking for a mature professional appearance.

```html
<!DOCTYPE html>
<html lang="en">
<head>
<meta charset="utf-8">
<title>Corvane Business Card</title>
<link rel="stylesheet" href="https://fonts.googleapis.com/css2?family=Open+Sans:wght@400&family=Kaushan+Script&display=swap">
<style>
  :root {
    --page: #dfe5f3;
    --navy-deep: #171b2d;
    --navy-glow: #26384f;
    --gold-dark: #a0722c;
    --gold-mid: #c89a33;
    --gold-light: #e3bb3a;
    --gold-text: #e8bd34;
    --ink: #111111;
    --paper-text: #e9e9ee;
    --rule: #8a8f9c;
  }
  * { margin: 0; padding: 0; box-sizing: border-box; }
  html, body { width: 1200px; height: 1000px; overflow: hidden; }
  body {
    background: var(--page);
    font-family: "Open Sans", sans-serif;
    position: relative;
    color: var(--paper-text);
  }
  .card {
    position: absolute;
    width: 412px;
    height: 721px;
    background: radial-gradient(ellipse 70% 55% at 50% 50%, var(--navy-glow) 0%, var(--navy-deep) 100%);
    overflow: hidden;
  }
  .card--front { left: 135px; top: 194px; }
  .card--back { left: 629px; top: 192px; }

  .gold-band {
    position: absolute;
    left: 0; width: 100%;
    background: linear-gradient(90deg, var(--gold-dark) 0%, var(--gold-mid) 35%, var(--gold-light) 55%, var(--gold-mid) 78%, var(--gold-dark) 100%);
  }
  .rule {
    position: absolute;
    height: 1px;
    background: var(--rule);
  }

  /* Front */
  .front-mark {
    position: absolute;
    left: 176px; top: 150px;
    width: 60px; height: 60px;
    border-radius: 50%;
    background: linear-gradient(90deg, var(--gold-dark), var(--gold-light));
  }
  .front-name {
    position: absolute;
    left: 0; width: 100%;
    top: 245px;
    text-align: center;
    font-size: 34px;
    letter-spacing: 10px;
    text-indent: 10px;
    color: var(--paper-text);
  }
  .card--front .gold-band { top: 399px; height: 65px; }
  .product-list {
    position: absolute;
    left: 0; width: 100%;
    top: 518px;
    list-style: none;
    text-align: center;
    font-size: 14.5px;
    line-height: 23px;
    letter-spacing: 3.4px;
    text-indent: 3.4px;
  }
  .card--front .rule { left: 72px; width: 270px; top: 643px; }
  .front-web {
    position: absolute;
    left: 0; width: 100%;
    top: 666px;
    text-align: center;
    font-size: 16.5px;
  }

  /* Back */
  .card--back .gold-band { top: 19px; height: 65px; }
  .band-name {
    position: absolute;
    left: 38px; top: 38px;
    font-size: 30px;
    line-height: 1;
    color: var(--ink);
  }
  .band-line {
    position: absolute;
    left: 210px; right: 0; top: 60px;
    height: 2px;
    background: var(--ink);
  }
  .person-name {
    position: absolute;
    left: 38px; top: 158px;
    font-family: "Kaushan Script", cursive;
    font-size: 56px;
    line-height: 1.2;
    color: var(--gold-text);
  }
  .card--back .rule { left: 38px; width: 271px; }
  .rule--top { top: 316px; }
  .rule--bottom { top: 621px; }
  .contact {
    position: absolute;
    left: 38px;
    font-size: 16.5px;
    line-height: 23px;
    font-style: normal;
  }
  .contact--phones { top: 360px; line-height: 29px; }
  .contact--email { top: 447px; }
  .contact--address { top: 508px; }
  .back-web {
    position: absolute;
    left: 38px; top: 662px;
    font-size: 16.5px;
    color: var(--gold-text);
  }
</style>
</head>
<body>
  <section class="card card--front" aria-label="Card front">
    <div class="front-mark"></div>
    <div class="front-name">CORVANE</div>
    <div class="gold-band"></div>
    <ul class="product-list">
      <li>HYDRAULIC ADAPTERS</li>
      <li>HOUSE FITTINGS</li>
      <li>QUICK COUPLINGS</li>
    </ul>
    <div class="rule"></div>
    <div class="front-web">www.corvanefittings.com</div>
  </section>

  <section class="card card--back" aria-label="Card back">
    <div class="gold-band"></div>
    <div class="band-name">Corvane</div>
    <div class="band-line"></div>
    <div class="person-name">Len Harwick</div>
    <div class="rule rule--top"></div>
    <address class="contact contact--phones">
      +86 135 2207 4419 (China)<br>
      +61 412 875 309 (Australia)
    </address>
    <address class="contact contact--email">lharwick@corvanefittings.com</address>
    <address class="contact contact--address">
      17 Jin Hua Tower 402 Qinglan<br>
      Road, Haishu District Ningbo<br>
      315000 China
    </address>
    <div class="rule rule--bottom"></div>
    <div class="back-web">www.corvanefittings.com</div>
  </section>
</body>
</html>
```